Need web design for our e-assessment company

We need a web design for our e-assessment company called Tavolo. We develop modern, web-based software for supporting the testing and examination process. The application is delivered as a SaaS solution.

The application helps our customers save time and money.

The design should communicate the following:

- Modern
- Innovation
- Security
- Performance

Attached you can find a screenshot of our application as well as some thoughts on the website.

We would like a front page as well as 1 sub page.

And lastly, one more website we draw inspiration from (on top of the ones mentioned in the attached document): http://www.plenaxo-demo.com/
Updates

Dear all,

I have updated the description with 1 more example of websites we like as well as added that we would like a front page and a sub page.

Thanks in advance.

Best regards,

Osmund

Target Market(s)

Our target groups are higher education and awarding organisations. Decision makers are mostly men age 45+.

Industry/Entity Type

It Company

Requirements
Must have
• 1 front page and 1 sub page

```html
<!DOCTYPE html>
<html lang="en">
<head>
<meta charset="utf-8">
<title>Tavolo – e-Assessment, Simplified</title>
<link rel="stylesheet" href="https://fonts.googleapis.com/css2?family=Questrial&family=Kalam:wght@400&family=Open+Sans:wght@400;600;700&display=swap">
<style>
:root{
  --orange:#f26b21;
  --orange-light:#f79a5c;
  --blue:#1aa5e0;
  --ink:#333;
  --muted:#666;
  --band:#ececec;
  --footer:#565656;
  --footer-field:#6b6b6b;
  --footer-text:#d8d8d8;
  --white:#fff;
  --icon-dark:#4a4a4a;
}
*{box-sizing:border-box;margin:0;padding:0}
html,body{width:1200px;height:3110px;overflow:hidden;background:var(--white)}
body{font-family:"Open Sans",Arial,sans-serif;color:var(--ink);position:relative}
.display{font-family:"Questrial",Arial,sans-serif}
section,header,footer{position:absolute;left:0;width:1200px}
.abs{position:absolute}

/* header */
.site-header{top:0;height:72px;background:var(--white)}
.brand{left:156px;top:14px;display:flex;align-items:center;gap:10px}
.brand-dot{width:42px;height:42px;border-radius:50%;background:var(--orange)}
.brand-name{font-family:"Questrial",sans-serif;font-size:34px;color:var(--ink)}
.main-nav{left:342px;top:26px;display:flex;gap:34px;font-family:"Questrial",sans-serif;font-size:16px}
.login{left:800px;top:22px;display:flex;align-items:center;gap:12px;font-family:"Questrial",sans-serif;font-size:16px}
.btn-contact{left:902px;top:20px;width:140px;height:34px;background:var(--blue);color:var(--white);font-family:"Questrial",sans-serif;font-size:16px;display:flex;align-items:center;justify-content:center}

/* hero */
.hero{top:72px;height:560px;background:linear-gradient(90deg,var(--orange-light) 0%,#f4803b 45%,var(--orange) 100%);overflow:hidden}
.promise{left:156px;display:flex;align-items:center;gap:22px;color:var(--white);font-family:"Questrial",sans-serif;font-size:22px}
.promise svg{width:127px;height:127px}
.hero-photo{left:478px;top:173px;width:635px;height:387px;background:linear-gradient(160deg,#d9d3cf 0%,#b9b4b2 50%,#efefef 100%);border-radius:4px 4px 0 0}
.tagline{left:575px;top:68px;font-family:"Kalam",cursive;font-size:50px;color:var(--white);letter-spacing:1px}
.btn-try{left:694px;top:162px;width:223px;height:44px;background:var(--blue);border:3px solid #5cc3ee;color:var(--white);font-family:"Questrial",sans-serif;font-size:22px;display:flex;align-items:center;justify-content:center}
.slide-arrow{top:258px;width:44px;height:44px;border:2px solid var(--white);border-radius:50%}

/* signup */
.signup{top:632px;height:138px;background:var(--band)}
.signup-title{left:156px;top:45px;font-family:"Questrial",sans-serif;font-size:34px;color:#444}
.btn-signup{left:562px;top:46px;width:232px;height:48px;background:var(--orange);color:var(--white);font-family:"Questrial",sans-serif;font-size:22px;display:flex;align-items:center;justify-content:center}
.social{left:858px;top:48px;display:flex;gap:26px}
.social span{width:44px;height:44px;border-radius:50%;background:#a5a5a5;display:block}

/* how it works */
.how{top:770px;height:425px}
.section-title{font-family:"Questrial",sans-serif;font-size:32px;color:#444}
.body-copy{font-size:12.5px;line-height:18px;color:var(--muted)}
.watch{left:156px;top:318px;font-family:"Kalam",cursive;font-size:26px;color:var(--orange);display:flex;align-items:center;gap:14px}
.video{left:703px;top:98px;width:339px;height:249px;background:linear-gradient(#e9e9e9,#d2d2d2);border:1px solid #ccc}
.video-bar{left:0;bottom:0;width:100%;height:36px;background:#555}

/* features */
.features{top:1195px;height:492px;background:var(--band)}
.app-screen{left:156px;top:78px;width:434px;height:270px;background:#1d1d1d;border-radius:10px;padding:14px}
.app-screen-inner{width:100%;height:100%;background:linear-gradient(180deg,#e9eef3 0%,#f8f9fb 100%);border-radius:2px}
.stand{left:326px;top:348px;width:94px;height:60px;background:linear-gradient(#d5d5d5,#9a9a9a);clip-path:polygon(15% 0,85% 0,100% 100%,0 100%)}
.feature-list{left:703px;top:156px;list-style:none}
.feature-list li{display:flex;align-items:center;gap:18px;height:46px;font-size:15px;color:#444}
.feature-list i{width:36px;height:36px;border-radius:50%;background:var(--orange);display:block;position:relative}

/* case studies */
.cases{top:1687px;height:376px}
.case{top:156px;display:flex;gap:12px}
.case-photo{width:133px;height:133px;border-radius:50%;background:linear-gradient(#e8e8e8,#c9c9c9);border:3px solid #ddd}
.case-name{font-size:12px;font-weight:700;color:var(--orange)}
.case-name b{color:#222;margin-left:8px}
.case-text{margin-top:14px;width:268px}
.read-more{color:var(--orange);font-size:12px}
.case-link{top:140px;width:16px;height:16px;border:2px solid #777;border-radius:50%}

/* partners */
.partners{top:2063px;height:190px;background:var(--band)}
.partner-row{left:156px;top:85px;width:886px;display:flex;justify-content:space-between;align-items:center}
.partner-badge{height:56px;background:#6a6a6a;border-radius:6px}

/* call to action */
.cta{top:2253px;height:253px;text-align:center}
.cta p{position:absolute;left:200px;top:52px;width:800px;font-family:"Questrial",sans-serif;font-size:22px;line-height:32px;color:#333}
.btn-start{left:407px;top:135px;width:383px;height:61px;background:var(--orange);color:var(--white);font-family:"Questrial",sans-serif;font-size:29px;display:flex;align-items:center;justify-content:center}

/* footer */
.site-footer{top:2506px;height:604px;background:var(--footer);color:var(--footer-text)}
.footer-title{font-family:"Questrial",sans-serif;font-size:20px;color:var(--white);padding-bottom:16px;border-bottom:1px solid #6e6e6e;width:234px}
.footer-copy{font-size:12px;line-height:16px;color:var(--footer-text);margin-top:20px;width:240px}
.field{width:243px;height:38px;background:var(--footer-field);margin-top:12px;font-size:12px;color:#cfcfcf;padding:10px 12px}
.field.message{height:140px}
.btn-send{width:109px;height:40px;background:#e4e4e4;color:#555;font-size:12px;margin-top:16px;display:flex;align-items:center;justify-content:center;gap:10px}
.tweet{width:234px;margin-top:18px;padding-bottom:18px;border-bottom:1px solid #6e6e6e;font-size:12px;line-height:16px}
.tweet a{color:var(--orange);text-decoration:none}
.tweet-meta{display:flex;gap:20px;align-items:center;margin-top:14px;color:var(--orange)}
.footer-icons{display:flex;gap:12px;margin-top:24px}
.footer-icons span{width:26px;height:26px;border-radius:50%;border:2px solid #888;display:block}
.footer-bar{left:156px;top:528px;width:886px;border-top:1px solid #6e6e6e;padding-top:30px;font-size:12px;display:flex;gap:48px}
.footer-bar em{font-style:normal;color:var(--orange)}
.to-top{left:1018px;top:556px}
</style>
</head>
<body>

<header class="site-header">
  <div class="brand abs"><span class="brand-dot"></span><span class="brand-name">Tavolo</span></div>
  <nav class="main-nav abs"><span>Home</span><span>How it works</span><span>Features</span><span>Pricing</span></nav>
  <div class="login abs">
    <svg width="22" height="24" viewBox="0 0 22 24"><path d="M5 10V7a6 6 0 0 1 12 0v3" fill="none" stroke="#444" stroke-width="3"/><rect x="2" y="10" width="18" height="14" rx="2" fill="#444"/></svg>
    <span>Login</span>
  </div>
  <a class="btn-contact abs">CONTACT US</a>
</header>

<section class="hero">
  <div class="promise abs" style="top:50px">
    <svg viewBox="0 0 127 127"><circle cx="63.5" cy="63.5" r="60" fill="var(--icon-dark)"/><g fill="#fff"><rect x="40" y="30" width="47" height="14" rx="2"/><rect x="40" y="48" width="47" height="14" rx="2"/><rect x="40" y="66" width="47" height="14" rx="2"/><rect x="61" y="80" width="5" height="12"/><rect x="38" y="92" width="51" height="5"/></g><line x1="10" y1="10" x2="117" y2="117" stroke="#d9d3cf" stroke-width="9"/></svg>
    <span>No servers.</span>
  </div>
  <div class="promise abs" style="top:215px">
    <svg viewBox="0 0 127 127"><circle cx="63.5" cy="63.5" r="60" fill="var(--icon-dark)"/><g stroke="#fff" stroke-width="9" stroke-linecap="round"><line x1="38" y1="88" x2="88" y2="38"/><line x1="38" y1="38" x2="88" y2="88"/></g><line x1="10" y1="10" x2="117" y2="117" stroke="#d9d3cf" stroke-width="9"/></svg>
    <span>No maintenance.</span>
  </div>
  <div class="promise abs" style="top:380px">
    <svg viewBox="0 0 127 127"><circle cx="63.5" cy="63.5" r="60" fill="var(--icon-dark)"/><circle cx="63.5" cy="63.5" r="30" fill="none" stroke="#fff" stroke-width="6"/><line x1="10" y1="10" x2="117" y2="117" stroke="#d9d3cf" stroke-width="9"/></svg>
    <span>No worries.</span>
  </div>
  <div class="hero-photo abs" role="img" aria-label="Photo of a smiling woman with a headset working at a desktop computer"></div>
  <div class="tagline abs">e-Assessment. Simplified</div>
  <a class="btn-try abs">TRY IT NOW!</a>
  <svg class="slide-arrow abs" style="left:107px" viewBox="0 0 44 44"><path d="M25 14l-8 8 8 8" fill="none" stroke="#fff" stroke-width="2.5"/></svg>
  <svg class="slide-arrow abs" style="left:1049px" viewBox="0 0 44 44"><path d="M19 14l8 8-8 8" fill="none" stroke="#fff" stroke-width="2.5"/></svg>
</section>

<section class="signup">
  <h2 class="signup-title abs">Sign up for a free demo</h2>
  <a class="btn-signup abs">SIGN UP NOW!</a>
  <div class="social abs"><span></span><span></span><span></span></div>
</section>

<section class="how">
  <h2 class="section-title abs" style="left:156px;top:92px">How it Works</h2>
  <p class="body-copy abs" style="left:156px;top:145px;width:412px">Etiam mattis tellus ut eleifend semper. Integer a velit urna. Cras mollis cursus ornare. Cras porta nunc lorem, at iaculis odio semper et. Suspendisse gravida metus arcu, vitae blandit sem euismod vel. In pellentesque libero quis tincidunt imperdiet. Mauris ut aliquet mauris, placerat aliquet augue. Ut velit mauris, lobortis sit amet dignissim ac, interdum a odio. Curabitur vel ante faucibus, interdum dui nec.<br><br>rutrum erat. Proin vel eros luctus, suscipit massa vel, sagittis neque. Aliquam tempor fermentum nisi, lacinia iaculis ipsum tempor eget.</p>
  <div class="watch abs">Watch the video
    <svg width="200" height="20" viewBox="0 0 200 20"><path d="M2 12 Q100 16 190 10" fill="none" stroke="#aaa" stroke-width="1.5"/><path d="M182 4l10 6-10 6" fill="none" stroke="#aaa" stroke-width="1.5"/></svg>
  </div>
  <div class="video abs">
    <svg class="abs" style="left:124px;top:62px" width="90" height="90" viewBox="0 0 90 90"><circle cx="45" cy="45" r="42" fill="none" stroke="#fff" stroke-width="4"/><path d="M36 27v36l28-18z" fill="#fff"/></svg>
    <div class="video-bar abs">
      <svg class="abs" style="left:6px;top:6px" width="44" height="24" viewBox="0 0 44 24"><rect width="44" height="24" fill="#333"/><path d="M17 6v12l10-6z" fill="#fff"/></svg>
      <div class="abs" style="left:62px;top:14px;width:220px;height:8px;background:#444;border:1px solid #777"></div>
      <div class="abs" style="left:292px;top:14px;width:24px;height:8px;background:#2a9fd6"></div>
    </div>
  </div>
</section>

<section class="features">
  <div class="app-screen abs"><div class="app-screen-inner" role="img" aria-label="Screenshot of the Tavolo assessment dashboard"></div></div>
  <div class="stand abs"></div>
  <div class="abs" style="left:156px;top:408px;width:434px;height:10px;border-radius:50%;background:#d8d8d8"></div>
  <h2 class="section-title abs" style="left:703px;top:80px">FEATURES</h2>
  <ul class="feature-list abs">
    <li><i></i>Create Questions</li>
    <li><i></i>Create Assessments</li>
    <li><i></i>Schedule Assessments</li>
    <li><i></i>Deliver Assessments to Candidates</li>
    <li><svg width="36" height="36" viewBox="0 0 36 36"><circle cx="18" cy="18" r="18" fill="var(--orange)"/><path d="M10 18l6 6 11-12" fill="none" stroke="#fff" stroke-width="3.5"/></svg>Mark these Assessments</li>
  </ul>
</section>

<section class="cases">
  <h2 class="section-title abs" style="left:156px;top:60px;font-size:28px">CASE STUDIES</h2>
  <div class="case abs" style="left:156px">
    <div class="case-photo" role="img" aria-label="Portrait photo of a customer"></div>
    <div>
      <div class="case-name">Marek Lindqvist - <b>www.samplecampus-demo.com</b></div>
      <p class="body-copy case-text">Etiam mattis tellus ut eleifend semper. Integer a velit urna. Cras mollis cursus ornare. Cras porta nunc lorem, at iaculis odio semper et. Suspendisse gravida metus arcu, vitae blandit sem euismod vel. In pellente.<br><span class="read-more">READ MORE [...]</span></p>
    </div>
  </div>
  <span class="case-link abs" style="left:214px;top:295px"></span>
  <div class="case abs" style="left:630px">
    <div class="case-photo" role="img" aria-label="Portrait photo of a customer"></div>
    <div>
      <div class="case-name">Hanna Oduya - <b>www.samplecampus-demo.com</b></div>
      <p class="body-copy case-text">Etiam mattis tellus ut eleifend semper. Integer a velit urna. Cras mollis cursus ornare. Cras porta nunc lorem, at iaculis odio semper et. Suspendisse gravida metus arcu, vitae blandit sem euismod vel. In pellente.<br><span class="read-more">READ MORE [...]</span></p>
    </div>
  </div>
  <span class="case-link abs" style="left:688px;top:295px"></span>
</section>

<section class="partners">
  <h2 class="section-title abs" style="left:156px;top:30px;font-size:27px">OUR PARTNERS</h2>
  <div class="partner-row abs">
    <span class="partner-badge" style="width:72px;border-radius:50%"></span>
    <span class="partner-badge" style="width:120px"></span>
    <span class="partner-badge" style="width:180px"></span>
    <span class="partner-badge" style="width:180px"></span>
    <span class="partner-badge" style="width:140px"></span>
  </div>
</section>

<section class="cta">
  <p>Etiam mattis tellus ut eleifend semper. Integer a velit urna. Cras mollis orta nunc lorem, at iaculis odio semper et.</p>
  <a class="btn-start abs">Getting Started</a>
</section>

<footer class="site-footer">
  <div class="abs" style="left:156px;top:56px">
    <h3 class="footer-title">ABOUT TAVOLO</h3>
    <p class="footer-copy">Lorem ipsum dolor sit amet, consectetur adipiscing elit. Aliquam nec congue neque. Integer et feugiat nibh. Ut pretium imperdiet ante ac feugiat.<br><br>Nullam eleifend leo urna, a sodales tellus gravida eu. Integer eu erat luctus, auctor lectus quis, tristique nulla. Phasellus aliquet a purus vel rhoncus. Fusce aliquam tortor lacinia, pulvinar nunc eu, mae suada turpis.</p>
    <div class="footer-icons"><span></span><span></span><span></span></div>
  </div>
  <div class="abs" style="left:476px;top:56px">
    <h3 class="footer-title">CONTACT FORM</h3>
    <div class="field" style="margin-top:14px">Name</div>
    <div class="field">Email</div>
    <div class="field">Phone</div>
    <div class="field message">Message</div>
    <div class="btn-send">SEND <svg width="14" height="14" viewBox="0 0 14 14"><path d="M0 7l14-7-4 14-3-5z" fill="var(--orange)"/></svg></div>
  </div>
  <div class="abs" style="left:808px;top:56px">
    <h3 class="footer-title">RECENT TWEETS</h3>
    <div class="tweet">@northbeamstudio Pls send me an <a>info@northbeamstudio-demo.com</a> (need email for account) and I can create an account for you. Thanks!
      <div class="tweet-meta"><svg width="22" height="16" viewBox="0 0 22 16"><path d="M1 12 Q11 16 20 3" fill="none" stroke="#888" stroke-width="3"/></svg>7 days ago</div>
    </div>
    <div class="tweet" style="border-bottom:0">@northbeamstudio Pls send me an <a>info@northbeamstudio-demo.com</a> (need email for account) and I can create an account for you. Thanks!
      <div class="tweet-meta"><svg width="22" height="16" viewBox="0 0 22 16"><path d="M1 12 Q11 16 20 3" fill="none" stroke="#888" stroke-width="3"/></svg>7 days ago</div>
    </div>
  </div>
  <div class="footer-bar abs"><span>Copyright © 2014 <em>TAVOLO</em></span><span>Terms &amp; Conditions | Privacy Policy</span></div>
  <svg class="to-top abs" width="24" height="20" viewBox="0 0 24 20"><path d="M12 2L2 14h7v6h6v-6h7z" fill="#e8e8e8"/></svg>
</footer>

</body>
</html>
```